Stellenanzeige Mechaniker für Baumaschinen
Zielgruppe
Was wir machen: Baumaschinenhandel und Vermietung
Was wir suchen: Vollzeitkräfte in der Werkstatt Service und Verkauf
www.baumaschinen-krosbach.de
www.krosbach-rental.de
Aufgabenstellung
Eyecatcher, die Anzeige soll in diversen Medien gestreut werden.
Ihr Aufgabengebiet
Zuverlässig umsetzen: Sie reparieren Neu- und Gebrauchtmaschinen im Außen- und Innendienst
Sicherheit schaffen: Durchführung von Inspektionen, UVV-Prüfungen und Wartungsarbeiten
Probleme beseitigen: Fehler- und Störungsanalyse
Werte entdecken: Aufarbeitung von Gebraucht- und Mietmaschinen
Kundenzufriedenheit garantieren: Aus- und Umrüsten vom Maschinen mit Zubehör Kundenbetreuung im Servicebereich sowie Ersatzteilbeschaffung und Garantieabwicklungen
Ihr Profil
Ausbildung: als Land-/Baumaschinenmechaniker oder vergleichbare Ausbildung
Persönlichkeit: kommunikatives und sympathisches Auftreten, hohes Qualitätsbewusstsein,
Arbeitsweise: selbständig, strukturiert, belastbar und zuverlässig
Erfahrungen und Knowhow: Einschlägige Berufserfahrung in der Branche, Sichere PC-Anwendung (Diagnose-Tools), Gute Kenntnisse in Hydraulik, Elektrik und Motoren
Mobilität: Führerschein Klasse B (Pkw)
Wir bieten:
Zukunfts- und krisensicherer Arbeitsplatz
Interessante und abwechslungsreiche Aufgaben in einer vertrauensvollen Arbeitsatmosphäre
Attraktive Vergütung
Fundierte und strukturierte Einarbeitung
Weiterbildungs- und Entwicklungsmöglichkeiten
Gutes Betriebsklima in einer familiären Atmosphäre
Kurze Entscheidungswege

```html
<!DOCTYPE html>
<html lang="de">
<head>
<meta charset="utf-8">
<title>Stellenanzeige – Mechaniker für Baumaschinen</title>
<link rel="stylesheet" href="https://fonts.googleapis.com/css2?family=Montserrat:wght@400;500;700&family=Anton&display=swap">
<style>
  :root {
    --ink: #111111;
    --accent-red: #e0141e;
    --footer-yellow: #ffe100;
    --paper: #ffffff;
    --hero-teal: #3fb7c4;
    --hero-sand: #cfc3b4;
    --hero-haze: #e8e2da;
  }
  * { margin: 0; padding: 0; box-sizing: border-box; }
  html, body { width: 848px; height: 1200px; overflow: hidden; background: var(--paper); }
  .ad {
    position: relative; width: 848px; height: 1200px; overflow: hidden;
    font-family: "Montserrat", sans-serif; color: var(--ink); background: var(--paper);
  }
  .hero {
    position: absolute; left: 0; top: 0; width: 848px; height: 338px;
    background:
      linear-gradient(180deg, rgba(255,255,255,0.15) 0%, rgba(255,255,255,0.35) 60%, rgba(255,255,255,0.1) 100%),
      linear-gradient(100deg, #b9d9e0 0%, var(--hero-haze) 30%, var(--hero-sand) 50%, var(--hero-teal) 75%, #2fa2ae 100%);
  }
  .brand-name {
    position: absolute; top: 22px; right: 34px;
    font-family: "Montserrat", sans-serif; font-weight: 700; font-size: 22px;
    letter-spacing: 1px; color: var(--ink); white-space: nowrap;
  }
  .display {
    position: absolute; left: 0; width: 848px; text-align: center;
    font-family: "Anton", sans-serif; font-weight: 400; color: var(--ink);
    text-shadow: 2px 1px 0 var(--accent-red);
    text-transform: uppercase; font-style: italic; line-height: 1; white-space: nowrap;
  }
  .display-kicker { top: 114px; font-size: 48px; letter-spacing: 1.5px; }
  .display-role { top: 207px; font-size: 45px; letter-spacing: 1.5px; }
  .section-title {
    position: absolute; font-family: "Anton", sans-serif; font-weight: 400; font-style: italic;
    text-transform: uppercase; font-size: 20px; line-height: 1; color: var(--ink);
    text-shadow: 1px 1px 0 var(--accent-red); white-space: nowrap;
  }
  .title-tasks { left: 8px; top: 357px; letter-spacing: 0.6px; }
  .title-profile { left: 32px; top: 610px; letter-spacing: 3.5px; }
  .title-offer { left: 33px; top: 905px; letter-spacing: 0.6px; }
  .list {
    position: absolute; font-size: 21.5px; line-height: 23px; text-align: justify;
    list-style: disc;
  }
  .list li::marker { font-size: 14px; }
  .list-tasks { left: 55px; top: 390px; width: 778px; }
  .list-profile { left: 50px; top: 659px; width: 780px; text-align: left; }
  .list-profile li { margin-bottom: 2.5px; }
  .list-offer { left: 50px; top: 941px; width: 776px; }
  .list-offer li { margin-bottom: 0.5px; }
  .footer { position: absolute; left: 0; top: 1177px; width: 848px; height: 23px; }
  .footer svg { position: absolute; left: 0; top: 0; }
  .footer-url {
    position: absolute; left: 59px; top: 3px; font-size: 14px; letter-spacing: 1.2px; color: var(--ink);
  }
</style>
</head>
<body>
<main class="ad">
  <div class="hero" role="img" aria-label="Foto: Servicetechniker an einem türkisfarbenen Kettenbagger auf einer Baustelle, links ein Servicefahrzeug mit gelber Rundumleuchte"></div>

  <span class="brand-name">KROSBACH BAUMASCHINEN</span>

  <h1 class="display display-kicker">Wir suchen</h1>
  <h2 class="display display-role">Mechaniker für Baumaschinen (m/w/d)</h2>

  <h3 class="section-title title-tasks">Ihr Aufgabengebiet</h3>
  <ul class="list list-tasks">
    <li>Zuverlässig umsetzen: Sie reparieren Neu- und Gebrauchtmaschinen im Außen- und Innendienst</li>
    <li>Sicherheit schaffen: Durchführung von Inspektionen, UVV-Prüfungen und Wartungsarbeiten</li>
    <li>Probleme beseitigen: Fehler- und Störungsanalyse</li>
    <li>Werte entdecken: Aufarbeitung von Gebraucht- und Mietmaschinen</li>
    <li>Kundenzufriedenheit garantieren: Aus- und Umrüsten vom Maschinen mit Zubehör Kundenbetreuung im Servicebereich sowie Ersatzteilbeschaffung und Garantieabwicklungen</li>
  </ul>

  <h3 class="section-title title-profile">Ihr Profil</h3>
  <ul class="list list-profile">
    <li>Ausbildung: als Land-/Baumaschinenmechaniker oder vergleichbare Ausbildung</li>
    <li>Persönlichkeit: kommunikatives und sympathisches Auftreten, hohes Qualitätsbewusstsein,</li>
    <li>Arbeitsweise: selbständig, strukturiert, belastbar und zuverlässig</li>
    <li>Erfahrungen und Knowhow: Einschlägige Berufserfahrung in der Branche, Sichere PC-Anwendung (Diagnose-Tools), Gute Kenntnisse in Hydraulik, Elektrik und Motoren</li>
    <li>Mobilität: Führerschein Klasse B (Pkw)</li>
  </ul>

  <h3 class="section-title title-offer">Wir bieten</h3>
  <ul class="list list-offer">
    <li>Zukunfts- und krisensicherer Arbeitsplatz</li>
    <li>Interessante und abwechslungsreiche Aufgaben in einer vertrauensvollen Arbeitsatmosphäre</li>
    <li>Attraktive Vergütung</li>
    <li>Fundierte und strukturierte Einarbeitung</li>
    <li>Weiterbildungs- und Entwicklungsmöglichkeiten</li>
    <li>Gutes Betriebsklima in einer familiären Atmosphäre</li>
    <li>Kurze Entscheidungswege</li>
  </ul>

  <footer class="footer">
    <svg width="848" height="23" viewBox="0 0 848 23" aria-hidden="true">
      <rect x="0" y="0" width="848" height="23" fill="#111111"/>
      <polygon points="0,0 468,0 491,23 0,23" fill="#ffe100"/>
    </svg>
    <span class="footer-url">https://www.baumaschinen-krosbach.de/</span>
  </footer>
</main>
</body>
</html>
```